BRIGHTWAVE DENTAL *

please see attached.

Target Market(s)

Adults 18-60

Contact Information for Business Card

Website: brightwavedentalqz.com
Phone number 555 304 7726 email: brightwavedentalqz@mailvex.com
Address:417 S. Kellim rd
Suite#24, TX70000
Dr. Elias Varno, DDS

Font styles to use
Sans Serif

Requirements
Must have
• Logo, phone number website, doctor,
• 's name

```html
<!DOCTYPE html>
<html lang="en">
<head>
<meta charset="utf-8">
<title>Brightwave Dental – Business Card</title>
<link rel="stylesheet" href="https://fonts.googleapis.com/css2?family=Montserrat:wght@300&family=Fira+Mono:wght@400;500&display=swap">
<style>
  :root {
    --teal: #0e8aa6;
    --teal-deep: #0b7d97;
    --ink: #2f2f2f;
    --paper: #ffffff;
    --backdrop: #e9ecee;
  }
  * { margin: 0; padding: 0; box-sizing: border-box; }
  html, body { width: 1200px; height: 1200px; overflow: hidden; }
  body {
    background: var(--backdrop);
    position: relative;
    font-family: "Fira Mono", monospace;
  }
  .card {
    position: absolute;
    left: 180px;
    width: 840px;
    height: 480px;
    box-shadow: 0 6px 18px rgba(0,0,0,0.18);
  }
  .card--back { top: 90px; background: var(--teal); }
  .card--front { top: 630px; background: var(--paper); }

  .brand {
    display: flex;
    align-items: center;
    gap: 18px;
    font-family: "Montserrat", sans-serif;
    font-weight: 300;
    letter-spacing: 0.04em;
    white-space: nowrap;
  }
  .brand__circle {
    border-radius: 50%;
    flex: none;
  }
  .card--back .brand {
    position: absolute;
    left: 0; right: 0; top: 50%;
    transform: translateY(-50%);
    justify-content: center;
    color: var(--paper);
    font-size: 44px;
  }
  .card--back .brand__circle {
    width: 84px; height: 84px;
    border: 2px solid var(--paper);
  }
  .card--front .brand {
    position: absolute;
    left: 34px; top: 112px;
    color: var(--ink);
    font-size: 30px;
  }
  .card--front .brand__circle {
    width: 62px; height: 62px;
    border: 2px solid var(--ink);
  }
  .divider {
    position: absolute;
    left: 436px; top: 180px;
    width: 2px; height: 230px;
    background: var(--teal);
  }
  .details {
    position: absolute;
    left: 462px; top: 196px;
    color: var(--ink);
  }
  .details__name {
    color: var(--teal);
    font-size: 31px;
    font-weight: 500;
    line-height: 1;
  }
  .details__title {
    font-size: 18px;
    letter-spacing: 0.06em;
    margin-top: 4px;
  }
  .contact {
    list-style: none;
    margin-top: 26px;
    font-size: 18px;
    line-height: 34px;
  }
  .contact li { display: flex; align-items: center; gap: 10px; }
  .contact svg { width: 20px; height: 20px; flex: none; }
  .contact__web { color: var(--teal); }
</style>
</head>
<body>
  <section class="card card--back" aria-label="Card back">
    <div class="brand">
      <span class="brand__circle"></span>
      <span class="brand__name">BRIGHTWAVE DENTAL</span>
    </div>
  </section>

  <section class="card card--front" aria-label="Card front">
    <div class="brand">
      <span class="brand__circle"></span>
      <span class="brand__name">BRIGHTWAVE DENTAL</span>
    </div>
    <div class="divider"></div>
    <div class="details">
      <p class="details__name">Dr. Elias Varno</p>
      <p class="details__title">DDS</p>
      <ul class="contact">
        <li>
          <svg viewBox="0 0 20 20" aria-hidden="true"><rect x="5" y="1.5" width="10" height="17" rx="2" fill="none" stroke="var(--teal)" stroke-width="2"/><circle cx="10" cy="15" r="1" fill="var(--teal)"/></svg>
          <span>555 304 7726</span>
        </li>
        <li>
          <svg viewBox="0 0 20 20" aria-hidden="true"><rect x="1" y="4" width="18" height="12" fill="var(--teal)"/><path d="M1 4 L10 11 L19 4" fill="none" stroke="#fff" stroke-width="1.5"/></svg>
          <span>ana@brightwavedentalqz.com</span>
        </li>
        <li>
          <svg viewBox="0 0 20 20" aria-hidden="true"><g fill="none" stroke="var(--teal)" stroke-width="1.4"><circle cx="10" cy="10" r="8.5"/><ellipse cx="10" cy="10" rx="3.8" ry="8.5"/><path d="M1.5 10 H18.5 M3 5.5 H17 M3 14.5 H17"/></g></svg>
          <span class="contact__web">brightwavedentalqz.com</span>
        </li>
      </ul>
    </div>
  </section>
</body>
</html>
```